Business Card and Letterhead Design for Public Accounting Firm

Business card and letterhead design for a CPA Firm located in Orange County, CA. We're looking for a modern and professional design utilizing our existing logo. We'd like a clean "less is more" look, but also something that catches the eye. We provide a high level of service to our clients. Open to single or double sided business cards.

Additional info: color numbers on logo
Blue :
R 0
G 83
B 125

#00537D

Silver :

R 154
G 154
B 154

#9A9A9A

Target Market(s)

Businesses and individuals

Industry/Entity Type

Accounting

Contact Information for Business Card

Moss Whitfield & Danby LLP - 4827 Larkspur Vale Road, Irvine, CA 92614 - (949)731-2864 - mwdaccts.example

Font styles to use
Serif
Sans Serif
Other font styles liked:
• See font file uploaded

Colors
0054AA
0677BA
7BADD7
CADEEF
E8F1F8

Requirements
Nice to have
• Possibly use the font file provided which matches our logo, but adjust to be not in all caps

```html
<!DOCTYPE html>
<html lang="en">
<head>
<meta charset="utf-8">
<title>Moss Whitfield &amp; Danby LLP — Stationery</title>
<link rel="stylesheet" href="https://fonts.googleapis.com/css2?family=Cinzel:wght@400;500&family=Montserrat:wght@400&display=swap">
<style>
  :root {
    --board: #999999;
    --navy: #00507d;
    --silver: #9a9a9a;
    --paper: #ffffff;
    --wash: #e8f1f8;
    --label: #ffffff;
  }
  * { margin: 0; padding: 0; box-sizing: border-box; }
  html, body { width: 1200px; height: 1200px; overflow: hidden; }
  body {
    position: relative;
    background: var(--board);
    font-family: "Cinzel", "Times New Roman", serif;
    color: var(--navy);
  }
  .divider {
    position: absolute; left: 599px; top: 0;
    width: 1px; height: 1083px; background: var(--navy);
  }
  .section-title {
    position: absolute;
    color: var(--label);
    font-size: 15px;
    letter-spacing: 0.5px;
    white-space: nowrap;
  }
  .section-title .num { font-size: 34px; margin-left: 8px; vertical-align: -3px; }

  /* Business cards */
  .card {
    position: absolute;
    width: 162px; height: 98px;
    background: var(--paper);
    box-shadow: 4px 6px 10px rgba(0,0,0,0.25);
    overflow: hidden;
  }
  .card.rounded { border-radius: 6px; }
  .card.back { background: var(--navy); color: var(--paper); }
  .card .name {
    position: absolute;
    font-size: 6.4px; line-height: 7.4px;
    letter-spacing: 0.8px;
    color: var(--navy);
    white-space: nowrap;
  }
  .card.back .name { color: var(--paper); }
  .card .wash {
    position: absolute; left: 0; right: 0; top: 34px; height: 46px;
    background: linear-gradient(180deg, rgba(232,241,248,0) 0%, var(--wash) 50%, rgba(232,241,248,0) 100%);
  }
  .card .band {
    position: absolute; left: 0; right: 0; bottom: 0;
    background: var(--navy);
  }
  .card .address {
    position: absolute;
    font-size: 3.6px; line-height: 6px;
    white-space: nowrap;
  }
  .card .site {
    position: absolute;
    font-size: 3.6px;
    white-space: nowrap;
  }

  /* Letterheads */
  .letterhead {
    position: absolute;
    width: 407px; height: 525px;
    background: var(--paper);
    box-shadow: 6px 8px 14px rgba(0,0,0,0.28);
    overflow: hidden;
  }
  .letterhead .name {
    position: absolute;
    font-size: 11.5px; line-height: 13.5px;
    letter-spacing: 1.6px;
    color: var(--navy);
    white-space: nowrap;
  }
  .letterhead .watermark {
    position: absolute; left: 0; right: 0; top: 210px;
    text-align: center;
    font-size: 58px; line-height: 62px;
    letter-spacing: 2px;
    color: var(--wash);
    white-space: nowrap;
  }
  .letterhead.second .watermark { color: #f1f5f9; }
  .letterhead .top-bar { position: absolute; background: var(--navy); }
  .letterhead .footer-text {
    position: absolute;
    font-size: 7px; line-height: 10.5px;
    white-space: nowrap;
  }
  .letterhead .site { position: absolute; font-size: 7px; white-space: nowrap; }
  .letterhead .bottom-band { position: absolute; left: 0; right: 0; bottom: 0; height: 13px; background: var(--navy); }

  /* Bottom banner */
  .banner {
    position: absolute; left: 0; top: 1083px;
    width: 1200px; height: 117px;
    background: var(--navy);
    font-family: "Montserrat", Arial, sans-serif;
  }
  .banner .enjoy {
    position: absolute; left: 129px; top: 28px;
    font-size: 48px; color: var(--silver); letter-spacing: -1px;
  }
  .banner .thanks {
    position: absolute; left: 802px; top: 22px;
    font-size: 54px; color: var(--paper); letter-spacing: 0;
  }
</style>
</head>
<body>
  <div class="divider"></div>

  <div class="section-title" style="left:379px; top:52px;">Business card<span class="num">1</span></div>
  <div class="section-title" style="left:659px; top:52px;">Business card<span class="num">2</span></div>

  <!-- Business card 1 -->
  <div class="card rounded" style="left:382px; top:114px;">
    <div class="wash"></div>
    <div class="name" style="left:13px; top:15px;">Moss Whitfield<br>&amp; Danby LLP</div>
    <div class="address" style="left:13px; top:66px;">Moss Whitfield &amp; Danby LLP<br>4827 Larkspur Vale Road<br>Irvine, CA (949)731-2864 · 92614</div>
    <div class="site" style="right:12px; top:79px;">mwdaccts.example</div>
    <div class="band" style="height:11px;"></div>
  </div>
  <div class="card rounded back" style="left:382px; top:245px;">
    <div class="name" style="left:46px; top:42px;">Moss Whitfield<br>&amp; Danby LLP</div>
    <div class="address" style="left:13px; top:78px;">Moss Whitfield &amp; Danby LLP<br>4827 Larkspur Vale Road<br>Irvine, CA (949)731-2864 · 92614</div>
    <div class="site" style="right:12px; top:90px;">mwdaccts.example</div>
  </div>

  <!-- Business card 2 -->
  <div class="card" style="left:656px; top:114px;">
    <div class="wash"></div>
    <div class="name" style="left:13px; top:15px;">Moss Whitfield<br>&amp; Danby LLP</div>
    <div class="band" style="height:21px;"></div>
    <div class="address" style="left:13px; top:80px; color:var(--paper);">Moss Whitfield &amp; Danby LLP · 4827 Larkspur Vale Road<br>Irvine, CA (949)731-2864 · 92614</div>
    <div class="site" style="right:15px; top:86px; color:var(--paper);">mwdaccts.example</div>
  </div>
  <div class="card back" style="left:656px; top:245px;">
    <div class="name" style="left:46px; top:42px;">Moss Whitfield<br>&amp; Danby LLP</div>
    <div class="address" style="left:13px; top:78px;">Moss Whitfield &amp; Danby LLP<br>4827 Larkspur Vale Road<br>Irvine, CA (949)731-2864 · 92614</div>
    <div class="site" style="right:12px; top:90px;">mwdaccts.example</div>
  </div>

  <div class="section-title" style="left:117px; top:437px;">LETTERHEAD<span class="num">1</span></div>
  <div class="section-title" style="left:703px; top:437px;">LETTERHEAD<span class="num">2</span></div>

  <!-- Letterhead 1 -->
  <div class="letterhead" style="left:116px; top:488px;">
    <div class="top-bar" style="left:220px; right:0; top:0; height:16px;"></div>
    <div class="name" style="left:28px; top:32px;">Moss Whitfield<br>&amp; Danby LLP</div>
    <div class="watermark">Moss Whitfield<br>&amp; Danby LLP</div>
    <svg width="170" height="36" viewBox="0 0 170 36" style="position:absolute; left:0; top:483px;">
      <path d="M0 0 H130 Q140 0 146 10 L146 12 H0 Z" fill="var(--silver)" opacity="0.6"/>
      <path d="M0 12 H148 Q162 12 168 34 V34 H0 Z" fill="var(--navy)"/>
    </svg>
    <div class="footer-text" style="left:181px; top:496px;">Moss Whitfield &amp; Danby LLP · 4827 Larkspur Vale Road<br>Irvine, CA (949)731-2864 · 92614</div>
    <div class="site" style="right:12px; top:506px;">mwdaccts.example</div>
  </div>

  <!-- Letterhead 2 -->
  <div class="letterhead second" style="left:696px; top:488px;">
    <div class="name" style="left:26px; top:32px;">Moss Whitfield<br>&amp; Danby LLP</div>
    <div class="top-bar" style="left:213px; right:0; top:33px; height:20px; border-radius:2px 0 0 2px;"></div>
    <div class="watermark">Moss Whitfield<br>&amp; Danby LLP</div>
    <div class="footer-text" style="left:15px; top:475px;">Moss Whitfield &amp; Danby LLP<br>4827 Larkspur Vale Road<br>Irvine, CA (949)731-2864 · 92614</div>
    <div class="site" style="right:21px; top:496px;">mwdaccts.example</div>
    <div class="bottom-band"></div>
  </div>

  <div class="banner">
    <div class="enjoy">ENJOY WATCHING</div>
    <div class="thanks">THANKS</div>
  </div>
</body>
</html>
```